Selvin: A Friday night in the Prophetic Flyer

We are holding 2 Friday night events, one on 10/25/19 and the other on 11/29/19.
The time frame is 6:30pm-9:00pm. These services will be a time of prayer/healing for the sick and will be prophetic as well. (There will be prophets prophesying over people)

The event is called: Selvin: A Friday night in the Prophetic
The flyer should also include the phrase/excerpt: "And they prophesied also".

Keywords/Phrases: Prophetic, Healing, Climbing in the Spirit, Higher level of Anointing...

Target Market(s)

those looking for healing, seeking a word from God

Colors

Designer to choose colors to be used in the design.

Requirements
Must have
• The event is called: Selvin: A Friday night in the Prophetic
• The flyer should also include the phrase/excerpt: "And they prophesied also".
• It must include the Tovik logo attached, either is fine, we have attached two different versions.
• It must have the dates, location, time
• Dates: October 25, 2019 and November 29, 2019
• Location: Hollard Community Center
• (Downtown Portland) 482 Wendle Street
• Portland, ME 04102
• Time: 6:30pm-9:00pm
• Contact Info: Tel. 207-555-3841
• email: contact@brimfield-hall.org
• web: www.tovik.org
Nice to have
• creativity in color scheme, the meaning of the word Selvin conveyed in a classy artistic way/design.
Should not have
• Crosses, pictures of churches

```html
<!DOCTYPE html>
<html lang="en">
<head>
<meta charset="utf-8">
<title>Selvin: A Friday Night in the Prophetic</title>
<link rel="stylesheet" href="https://fonts.googleapis.com/css2?family=Cinzel:wght@400;700&family=Montserrat:wght@400;500;700&display=swap">
<style>
  :root {
    --page: #ffffff;
    --indigo-deep: #1b1460;
    --indigo-band: #221a6e;
    --indigo-mid: #6d69ab;
    --lavender: #e6e4f1;
    --mist: #f3f2f8;
    --logo-navy: #0b2f55;
    --pill-top: #ffffff;
    --pill-bottom: #d9d8e2;
    --white: #ffffff;
    --footer-bg: #ecebf3;
  }
  * { margin: 0; padding: 0; box-sizing: border-box; }
  html, body {
    width: 1200px; height: 1000px; overflow: hidden;
    background: var(--page);
  }
  .flyer {
    position: absolute; left: 261px; top: 20px;
    width: 678px; height: 960px; overflow: hidden;
    font-family: "Montserrat", sans-serif;
    color: var(--white);
    text-align: center;
  }
  .hero-photo {
    position: absolute; left: 0; top: 0; width: 678px; height: 909px;
    background:
      radial-gradient(ellipse 60% 30% at 50% 48%, rgba(255,255,255,0.75), rgba(255,255,255,0) 70%),
      linear-gradient(180deg, var(--lavender) 0%, var(--mist) 30%, var(--indigo-mid) 58%, var(--indigo-band) 75%, var(--indigo-deep) 100%);
  }
  .brand-tab {
    position: absolute; left: 289px; top: 0; width: 101px; height: 117px;
    background: var(--logo-navy);
    display: flex; align-items: center; justify-content: center;
  }
  .brand-name {
    font-family: "Cinzel", serif; font-weight: 400;
    font-size: 22px; color: var(--white); letter-spacing: 0.02em;
  }
  .event-title {
    position: absolute; left: 0; width: 100%; top: 138px;
    font-family: "Cinzel", serif; font-weight: 700;
    font-size: 112px; line-height: 1; color: var(--indigo-deep);
    text-shadow: 3px 4px 0 rgba(200,198,225,0.9);
  }
  .event-subtitle {
    position: absolute; left: 0; width: 100%; top: 244px;
    font-family: "Cinzel", serif; font-weight: 400;
    font-size: 43px; line-height: 40px; color: var(--indigo-deep);
  }
  .scripture {
    position: absolute; left: 0; width: 100%; top: 329px;
    font-size: 12px; font-weight: 500; letter-spacing: 0.42em;
    color: var(--indigo-deep);
  }
  .pill {
    position: absolute; height: 34px; border-radius: 7px;
    background: linear-gradient(180deg, var(--pill-top), var(--pill-bottom));
    color: var(--indigo-deep); font-weight: 700;
    font-size: 23px; line-height: 34px;
  }
  .pill-dates { left: 158px; width: 362px; top: 635px; }
  .pill-time { left: 170px; width: 340px; top: 759px; }
  .venue {
    position: absolute; left: 0; width: 100%; top: 679px;
    font-size: 26px; font-weight: 700; letter-spacing: 0.06em;
  }
  .rule {
    position: absolute; height: 0;
    border-top: 3px dotted rgba(255,255,255,0.85);
  }
  .rule-wide { left: 66px; width: 546px; top: 716px; }
  .rule-short { left: 172px; width: 333px; top: 853px; }
  .address {
    position: absolute; left: 0; width: 100%; top: 726px;
    font-size: 19px; font-weight: 500;
  }
  .keywords {
    position: absolute; left: 0; width: 100%; top: 806px;
    font-size: 14.5px; line-height: 18px; font-weight: 500;
  }
  .details {
    position: absolute; left: 0; width: 100%; top: 868px;
    font-size: 12px; line-height: 15px; font-weight: 500;
  }
  .contact-bar {
    position: absolute; left: 0; top: 909px; width: 678px; height: 51px;
    background: var(--footer-bg); color: var(--indigo-deep);
    font-size: 14.5px; font-weight: 500; line-height: 51px;
  }
</style>
</head>
<body>
  <article class="flyer">
    <div class="hero-photo" role="img" aria-label="Worship crowd with raised hands in bright stage light, with two white doves flying near the top"></div>

    <div class="brand-tab"><span class="brand-name">TOVIK</span></div>

    <h1 class="event-title">SELVIN</h1>
    <p class="event-subtitle">A FRIDAY NIGHT IN<br>THE PROPHETIC</p>
    <p class="scripture">"AND THEY PROPHESIED ALSO"</p>

    <p class="pill pill-dates">OCT.25.19 AND NOV.29.19</p>
    <p class="venue">AT HOLLARD COMMUNITY CENTER</p>
    <div class="rule rule-wide"></div>
    <p class="address">482 WENDLE STREET, PORTLAND, ME 04102</p>
    <p class="pill pill-time">TIME: 6:30PM-9:00PM</p>

    <p class="keywords">PROPHETIC | HEALING<br>CLIMBING IN THE SPIRIT | HIGHER LEVEL OF ANOINTING</p>
    <div class="rule rule-short"></div>
    <p class="details">THESE SERVICES WILL BE A TIME OF PRAYER/HEALING FOR THE SICK AND<br>WILL BE PROPHETIC AS WELL. (THERE WILL BE PROPHETS PROPHESYING OVER PEOPLE)</p>

    <footer class="contact-bar">TEL. 207-555-3841 | EMAIL: CONTACT@BRIMFIELD-HALL.ORG | WWW.TOVIK.ORG</footer>
  </article>
</body>
</html>
```